Fennick Grove Gummy Bottle Label Design

(see attached word doc for full project description and example labels we like)
PROJECT OVERVIEW:
Fennick Grove is a healthy blend of functional organic super mushroom gummies that aims to enhance mood and promote overall mental and physical well-being by taking daily doses. The gummy product line offers a range of benefits, including increased energy, focus, calmness, sleep, immunity defense and overall mood upliftment. Fennick Grove is a brand that exudes positivity, vitality and personal growth. Fennick Grove is accessible, friendly, and approachable, making it easy for customers to integrate the brand into their daily routine. We cater/celebrate self-care by tending to both mental health and physical health.

Each benefit (i.e. product & flavor) is assigned a specific color that represents that “mood.” There are a total of 6 Moods, all 6 colors must be cohesive together. We prefer the color that represents the Mood to also be a clear representation of the flavor assigned to that mood, but we are open to interpretation if the color story looks good. We are also open to imagery (either real images or flaticons representing the ingredients or flavors) on the labels to help illustrate the components of this delicious product.

LABEL REQUEST:
The Fennick Grove products are gummies that will be placed in bottles and bags. There will be 6 different products with designated moods and flavors (i.e. Sleep/Lavender Vanilla, Calm/blackberry, Uplift/Pineapple, Focus/peach, Defense/black cherry, Energy/orange).

Dimensions will vary, here are a few:
Bottles:
6" W x 2" H
5" W x 2" H

Pouches:
4 x 6 x 2"

PRODUCTS:

Uplifting
Flavor: Pineapple
Mood: Mood Enhancement, Mental Health Helper
Front Label Ingredients: Cordyceps
Back Label Ingredients: Magnesium, Vitamin B2, Theacrine, Rhodiola Rosea, Shiitake, Cordyceps, Myrcene, Pinene.

Focus
Flavor: Sunny Plume
Mood: Focused, Creative, Productive
Front Label Ingredients: Lion’s Mane & Cordyceps
Back Label Ingredients: Rhodiola Rosea, Theacrine, Luteolin, Forskolin, Lions Mane, Cordyceps, Caryphyllene, Linalool.

Defense
Flavor: Black Cherry
Mood: Immunity & Gut Health
Front Label Ingredients: Turkey Tail
Back Label Ingredients: Vit A, Vit C, Ginger, Magnesium Glycinate, Lemon Balm, Maitake, Turkey Tail, Humulene.

Energy
Flavor: Rocket Parade
Mood: Awake, Stamina, Active
Front Label Ingredients: Lions Mane & Cordyceps
Back Label Ingredients: (NALT) N-Acetylcysteine-L-Tyrosine NALT, Caffeine, Vitamin B1, B3, Rhodiola Rosea, Ginkgo, Cordyceps, Valencene, Lions Mane, Limonene.

Sleep
Flavor: Vanilla Lavender Marlow Tide blend
Mood: Bedtime, Naptime, Relax Time
Front Label Ingredients: Melatonin & Reishi
Back Label Ingredients: Melatonin, Ashwagandha, Reishi, Bobinsana, Passion Flower, Linalool.

Calm
Flavor: Juniper Reel
Mood: Chill, Relaxed, Good Vibes
Front Label Ingredients: Reishi & Ashwagandha
Back Label Ingredients: Ashwagandha, Lemon Balm, Reishi, Chamomile, Velvet Bean, Caryophyllene.

```html
<!DOCTYPE html>
<html lang="en">
<head>
<meta charset="utf-8">
<title>Fennick Grove Gummy Labels</title>
<link rel="stylesheet" href="https://fonts.googleapis.com/css2?family=Open+Sans:wght@400;600;700;800&display=swap">
<style>
  :root {
    --page-bg: #ffffff;
    --ink: #ffffff;
    --uplift-main: #dcc00f;
    --uplift-edge: #cfb20c;
    --uplift-band: #c6a912;
    --focus-main: #f26d48;
    --focus-edge: #e85d38;
    --focus-band: #df4f1e;
  }
  * { box-sizing: border-box; margin: 0; padding: 0; }
  html, body {
    width: 1200px; height: 952px; overflow: hidden;
    background: var(--page-bg);
    font-family: "Open Sans", Arial, sans-serif;
    color: var(--ink);
  }
  .label-row {
    position: absolute; left: 40px; top: 241px;
    display: flex; gap: 40px;
  }
  .label {
    position: relative; width: 540px; height: 470px;
  }
  .label--uplift { background: linear-gradient(90deg, var(--uplift-edge), var(--uplift-main) 45%, var(--uplift-edge)); --band: var(--uplift-band); }
  .label--focus { background: linear-gradient(90deg, var(--focus-edge), var(--focus-main) 45%, var(--focus-edge)); --band: var(--focus-band); }

  .brand {
    position: absolute; top: 48px; left: 0; right: 0;
    display: flex; justify-content: center; align-items: center; gap: 10px;
    font-weight: 800; font-size: 30px; letter-spacing: 0.5px;
  }
  .brand-dot { width: 14px; height: 14px; border-radius: 50%; background: var(--ink); }

  .mood-title {
    position: absolute; top: 118px; left: 0; right: 0; text-align: center;
    font-weight: 700; font-size: 72px; line-height: 1; letter-spacing: -1px;
  }
  .product-band {
    position: absolute; top: 218px; left: 50px; width: 440px; height: 56px;
    background: var(--band);
    text-align: center; font-weight: 700; font-size: 34px; line-height: 52px;
  }
  .benefits {
    position: absolute; top: 288px; left: 0; right: 0; text-align: center;
    font-weight: 700; font-size: 19px;
  }
  .benefits .sep { font-weight: 400; margin: 0 6px; }

  .ingredients {
    position: absolute; top: 338px; left: 64px;
    font-weight: 700; font-size: 26px; line-height: 1.3;
  }
  .flavor {
    position: absolute; left: 64px;
    font-weight: 700; font-size: 19px; line-height: 1.2;
  }
  .label--uplift .flavor { top: 385px; }
  .label--focus .flavor { top: 412px; }

  .fruit-art {
    position: absolute; top: 340px; left: 232px; width: 86px; height: 112px;
    border-radius: 40px; background: rgba(255,255,255,0.82);
  }
  .label--focus .fruit-art { left: 262px; top: 350px; width: 86px; height: 100px; border-radius: 46px; }

  .dose-badge {
    position: absolute; top: 342px; left: 352px; width: 92px; height: 54px;
    border-radius: 10px; background: var(--band);
    text-align: center; font-weight: 800; line-height: 1;
  }
  .label--focus .dose-badge { left: 380px; top: 354px; }
  .dose-badge .amount { display: block; font-size: 20px; margin-top: 8px; }
  .dose-badge .unit { display: block; font-size: 12px; margin-top: 4px; }

  .count {
    position: absolute; top: 412px; left: 352px;
    font-weight: 400; font-size: 13px; line-height: 1.35;
  }
  .label--focus .count { left: 380px; top: 424px; }
</style>
</head>
<body>
  <main class="label-row">
    <section class="label label--uplift">
      <div class="brand"><span class="brand-dot"></span><span>Fennick Grove</span></div>
      <h1 class="mood-title">uplifting</h1>
      <div class="product-band">mushroom gummies</div>
      <p class="benefits">Mood Enhancement<span class="sep">|</span>Mental Health Helper</p>
      <p class="ingredients">Cordyceps</p>
      <p class="flavor">pineapple<br>flavor</p>
      <div class="fruit-art" role="img" aria-label="Pineapple flavor illustration"></div>
      <div class="dose-badge"><span class="amount">1000mg</span><span class="unit">PER GUMMY</span></div>
      <p class="count">8 Flavored Gummies<br>(1 oz)</p>
    </section>

    <section class="label label--focus">
      <div class="brand"><span class="brand-dot"></span><span>Fennick Grove</span></div>
      <h1 class="mood-title">focus</h1>
      <div class="product-band">mushroom gummies</div>
      <p class="benefits">Focused<span class="sep">|</span>Creative<span class="sep">|</span>Productive</p>
      <p class="ingredients">Lion’s Mane &amp;<br>Cordyceps</p>
      <p class="flavor">sunny plume<br>flavor</p>
      <div class="fruit-art" role="img" aria-label="Peach flavor illustration"></div>
      <div class="dose-badge"><span class="amount">1000mg</span><span class="unit">PER GUMMY</span></div>
      <p class="count">8 Flavored Gummies<br>(1 oz)</p>
    </section>
  </main>
</body>
</html>
```